Plumbing Van Vehicle Signage

I need a design for vehicle signage for a group of plumbing vans. The company name is 'Kestrel Gas & Plumbing'. I do all types of plumbing and gas fitting but specialise in general maintenance plumbing and gas fitting.

Industry/Entity Type

Plumbing

Requirements
Must have
• Must be eye catching. Must be able to go on a white back ground as the vans are white. Must contain phone number

```html
<!DOCTYPE html>
<html lang="en">
<head>
<meta charset="utf-8">
<title>Kestrel Gas &amp; Plumbing — Van Signage</title>
<link href="https://fonts.googleapis.com/css2?family=Michroma&family=Russo+One&display=swap" rel="stylesheet">
<style>
  :root {
    --page: #eef0f2;
    --panel: #ffffff;
    --panel-edge: #d4d8dc;
    --brand-blue: #2d3fa6;
    --brand-orange: #f28c1a;
    --steel: #8a8d91;
    --steel-dark: #5f6266;
    --white: #ffffff;
  }
  html, body {
    margin: 0;
    padding: 0;
    width: 899px;
    height: 1200px;
    overflow: hidden;
    background: var(--page);
  }
  .signage {
    width: 899px;
    height: 1200px;
    display: flex;
    flex-direction: column;
  }
  .van-side {
    display: block;
    width: 899px;
    height: 600px;
  }
  .van-body { fill: var(--panel); stroke: var(--panel-edge); stroke-width: 2; }
  .swoosh { fill: url(#steelFade); }
  .swoosh-flip { fill: url(#steelFadeFlip); }
  .band-blue { fill: var(--brand-blue); }
  .band-steel { fill: var(--steel-dark); }
  .rule-orange { fill: var(--brand-orange); }
  .brand-name {
    font-family: "Russo One", sans-serif;
    fill: var(--brand-blue);
  }
  .brand-name--main { font-size: 46px; letter-spacing: 1px; }
  .brand-name--sub { font-size: 19px; letter-spacing: 1.5px; }
  .web {
    font-family: "Michroma", sans-serif;
    font-size: 12px;
    letter-spacing: 5px;
    fill: var(--white);
  }
  .phone {
    font-family: "Michroma", sans-serif;
    font-size: 22px;
    letter-spacing: 1px;
    fill: var(--white);
    font-weight: 700;
  }
</style>
</head>
<body>
<main class="signage">

  <!-- Driver side: vehicle facing left -->
  <svg class="van-side van-side--driver" viewBox="0 0 899 600" xmlns="http://www.w3.org/2000/svg">
    <defs>
      <linearGradient id="steelFade" x1="0" x2="1" y1="0" y2="0">
        <stop offset="0" stop-color="#6d7074"/>
        <stop offset="1" stop-color="#b9bcbf"/>
      </linearGradient>
      <linearGradient id="steelFadeFlip" x1="1" x2="0" y1="0" y2="0">
        <stop offset="0" stop-color="#6d7074"/>
        <stop offset="1" stop-color="#b9bcbf"/>
      </linearGradient>
    </defs>
    <rect class="van-body" x="60" y="160" width="780" height="250" rx="26"/>
    <polygon class="swoosh" points="62,338 62,310 420,250 420,282"/>
    <g class="sign-block" transform="rotate(-13 640 300)">
      <text class="brand-name brand-name--main" x="512" y="262">KESTREL</text>
      <rect class="rule-orange" x="512" y="272" width="26" height="3"/>
      <text class="brand-name brand-name--sub" x="546" y="282">GAS &amp; PLUMBING</text>
      <rect class="rule-orange" x="770" y="272" width="26" height="3"/>
      <rect class="band-steel" x="470" y="296" width="360" height="20"/>
      <text class="web" x="500" y="311">www.kestrelgas.com</text>
      <rect class="rule-orange" x="440" y="320" width="390" height="4"/>
      <polygon class="band-blue" points="420,330 830,330 830,366 440,366"/>
      <text class="phone" x="452" y="357">Call: 000 000 0000</text>
    </g>
  </svg>

  <!-- Passenger side: vehicle facing right -->
  <svg class="van-side van-side--passenger" viewBox="0 0 899 600" xmlns="http://www.w3.org/2000/svg">
    <rect class="van-body" x="60" y="190" width="780" height="250" rx="26"/>
    <polygon class="swoosh-flip" points="838,370 838,342 480,282 480,314"/>
    <g class="sign-block" transform="rotate(12 300 300)">
      <text class="brand-name brand-name--main" x="220" y="262">KESTREL</text>
      <rect class="rule-orange" x="220" y="272" width="26" height="3"/>
      <text class="brand-name brand-name--sub" x="254" y="282">GAS &amp; PLUMBING</text>
      <rect class="rule-orange" x="478" y="272" width="26" height="3"/>
      <rect class="band-steel" x="70" y="296" width="380" height="20"/>
      <text class="web" x="100" y="311">www.kestrelgas.com</text>
      <rect class="rule-orange" x="70" y="320" width="400" height="4"/>
      <polygon class="band-blue" points="70,330 470,330 490,366 70,366"/>
      <text class="phone" x="92" y="357">Call: 000 000 0000</text>
    </g>
  </svg>

</main>
</body>
</html>
```